ecommerce news podcast artwork

Podcast cover art for a podcast featuring daily news and events around ecommerce product businesses.

text to be: VORLA BEAT
optional third line of text with smaller font: Podcast

looking for something that pops with a medium to light blue background. text can be in white/red/orange colors. prefer solid colors for text, but background can vary.
I'm really open to other ideas too, sometimes you don't know what you want until you see it.

Target Market(s)

ecommerce business owners, managers

Industry/Entity Type

news, business, ecommerce

Font styles to use
Sans Serif

Colors
0054AA
0677BA
7BADD7
CADEEF
E8F1F8
0094D4
00A9DD
6FCCEA
C7EBF8
E9F6FB
F0912C
F2A743
F7CA91
FBE8D2
FDF5EE
EB3D1F
EC4F4E
F09395
F8D3D4
FCEDEE

Requirements
Must have
• text: VORLA BEAT
Should not have
• no microphones, headsets/headphones, speakers, or other props like that.

```html
<!DOCTYPE html>
<html lang="en">
<head>
<meta charset="utf-8">
<title>Vorla Beat Podcast Cover</title>
<link rel="stylesheet" href="https://fonts.googleapis.com/css2?family=Montserrat:wght@800&display=swap">
<style>
  :root {
    --page-bg: #7a7a7a;
    --cover-blue: #82dcec;
    --frame-white: #ffffff;
    --title-red: #ff0d1e;
  }
  html, body {
    margin: 0;
    padding: 0;
    width: 1200px;
    height: 904px;
    overflow: hidden;
    background: var(--page-bg);
  }
  .stage {
    width: 1200px;
    height: 904px;
    display: flex;
    align-items: center;
    justify-content: center;
  }
  .cover {
    display: block;
    width: 840px;
    height: 840px;
  }
  .cover-bg { fill: var(--cover-blue); }
  .cover-frame { fill: none; stroke: var(--frame-white); stroke-width: 2.5; }
  .cover-title {
    font-family: "Montserrat", sans-serif;
    font-weight: 800;
    font-size: 140px;
    fill: var(--title-red);
  }
  .cover-subtitle {
    font-family: "Montserrat", sans-serif;
    font-weight: 800;
    font-size: 38px;
    letter-spacing: 16px;
    fill: var(--title-red);
  }
</style>
</head>
<body>
  <main class="stage">
    <svg class="cover" viewBox="0 0 840 840" xmlns="http://www.w3.org/2000/svg" aria-label="Vorla Beat Podcast">
      <rect class="cover-bg" x="0" y="0" width="840" height="840"/>
      <rect class="cover-frame" x="23" y="23" width="794" height="794"/>
      <text class="cover-title" x="420" y="370" text-anchor="middle">VORLA</text>
      <text class="cover-title" x="420" y="520" text-anchor="middle">BEAT</text>
      <text class="cover-subtitle" x="428" y="600" text-anchor="middle">PODCAST</text>
    </svg>
  </main>
</body>
</html>
```